Professional Commercial Cleaning Services

this website https://plomverservices.com.au/ already exists we just need someone to redesign and edit it. We had started this but not entirely sure how to design this ourselves.

We are a professional commercial cleaning business specialising in office, warehouse and restaurant cleaning. We would like to keep colours to black and white but are open to suggestions.

```html
<!DOCTYPE html>
<html lang="en">
<head>
<meta charset="utf-8">
<title>Plomver Services – Jobs</title>
<link href="https://fonts.googleapis.com/css2?family=Montserrat:wght@400;500;600;700;800&display=swap" rel="stylesheet">
<style>
:root{
  --navy:#16233f;
  --navy-deep:#132240;
  --orange:#f7921e;
  --teal:#1fa39a;
  --ink:#1c2333;
  --muted:#a8adb6;
  --line:#d9dce1;
  --white:#ffffff;
  --red:#e5322d;
}
*{box-sizing:border-box;margin:0;padding:0}
html,body{width:1200px;height:2167px;overflow:hidden}
body{position:relative;font-family:'Montserrat',sans-serif;color:var(--ink);background:var(--white)}
.hero{position:absolute;left:0;top:0;width:1200px;height:253px;background:linear-gradient(120deg,#2a3857 0%,#1d2a48 45%,#283654 100%)}
.brand{position:absolute;display:flex;align-items:center;gap:8px;font-weight:700;font-size:20px;color:var(--teal)}
.brand .dot{width:14px;height:14px;border-radius:50%;background:var(--teal)}
.site-header .brand{left:162px;top:38px}
.nav{position:absolute;top:42px;left:420px;display:flex;gap:33px;font-size:11.5px;font-weight:700;color:var(--white)}
.nav .active{color:var(--orange)}
.header-phone{position:absolute;left:942px;top:40px;font-size:15px;font-weight:700;color:var(--orange)}
.card{position:absolute;left:238px;top:172px;width:725px;height:1348px;background:var(--white);border-radius:10px;box-shadow:0 2px 10px rgba(20,30,60,.12)}
.form{position:absolute;left:0;top:0;width:1200px;height:1520px}
.form-title{position:absolute;left:319px;top:235px;font-size:19px;font-weight:800;color:var(--navy)}
.label{position:absolute;font-size:10px;font-weight:500;line-height:12.5px;color:var(--ink)}
.label sup,.req{color:var(--red);font-size:7px;vertical-align:top}
.field{position:absolute;height:23px;border:1px solid var(--line);border-radius:2px;font-size:8px;color:var(--muted);display:flex;align-items:center;padding:0 6px;gap:6px}
.field.wide{width:251px}
.field.half{width:250px}
.field .chev{margin-left:auto}
.flag{width:18px;height:11px;border-radius:2px;background:#c8ccd3}
.area{position:absolute;left:319px;width:562px;height:81px;border:1px solid var(--line);border-radius:2px}
.check{position:absolute;display:flex;align-items:center;gap:6px;font-size:10px}
.check i{width:12px;height:12px;border:1px solid #b9bdc4;border-radius:1px;display:block}
.note{position:absolute;left:319px;font-size:8px;color:#6a7080}
.drop{position:absolute;left:319px;top:1180px;width:562px;height:81px;border:1px dashed var(--line);display:flex;align-items:center;justify-content:center;gap:10px}
.drop span{font-size:6px;font-weight:600;color:#6a7080}
.drop b{background:var(--teal);color:var(--white);font-size:10px;font-weight:500;padding:7px 12px;border-radius:14px}
.small-caps{position:absolute;left:319px;top:1314px;font-size:7.5px;font-weight:700;letter-spacing:.5px}
.captcha{position:absolute;left:319px;top:1332px;width:212px;height:44px;border:1px solid var(--line);border-radius:2px;display:flex;align-items:center;padding:0 12px;gap:8px;font-size:10px}
.captcha i{width:14px;height:14px;border:1px solid #b9bdc4;display:block}
.captcha .mark{margin-left:auto;width:14px;height:14px;background:#c8ccd3;border-radius:2px}
.submit{position:absolute;left:319px;top:1415px;width:562px;height:36px;border-radius:18px;background:var(--orange);color:var(--white);font-size:12px;font-weight:500;display:flex;align-items:center;justify-content:center}
.cta{position:absolute;left:0;top:1583px;width:1200px;height:329px;background:linear-gradient(90deg,#2aa69a 0%,#7faa7c 35%,#d9a835 65%,#eaa21f 100%)}
.cta h2{position:absolute;left:162px;top:96px;font-size:33px;line-height:39px;font-weight:700;color:var(--white)}
.btn{position:absolute;top:194px;height:31px;border-radius:16px;color:var(--white);font-size:10px;font-weight:700;display:flex;align-items:center;justify-content:center}
.btn.teal{left:162px;width:103px;background:var(--teal)}
.btn.orange{left:278px;width:160px;background:var(--orange)}
.footer{position:absolute;left:0;top:1912px;width:1200px;height:255px;background:var(--navy-deep);color:var(--white)}
.footer .brand{left:162px;top:58px}
.contacts{position:absolute;right:162px;top:96px;display:flex;gap:24px;font-size:10px}
.contacts a{color:var(--white);display:flex;align-items:center;gap:10px}
.rule{position:absolute;left:162px;top:139px;width:876px;height:1px;background:#2e4466}
.copy{position:absolute;left:165px;top:164px;font-size:8.5px}
.links{position:absolute;right:162px;top:164px;display:flex;gap:27px;font-size:8.5px}
</style>
</head>
<body>
<header class="site-header">
  <div class="hero" role="img" aria-label="Photo of a person working at a laptop, dark blue tint"></div>
  <div class="brand"><span class="dot"></span>plomver services</div>
  <nav class="nav"><span>Home</span><span>About Us</span><span>Services</span><span>Why choose us</span><span class="active">Jobs</span><span>Contact Us</span></nav>
  <div class="header-phone">0400123987</div>
</header>

<main>
  <div class="card"></div>
  <section class="form">
    <h1 class="form-title">APPLICATION FOR CASUAL CLEANING POSITION</h1>

    <div class="label" style="left:319px;top:289px">First Name<sup>*</sup></div>
    <div class="field wide" style="left:319px;top:308px">First Name</div>
    <div class="label" style="left:619px;top:289px">Last Name<sup>*</sup></div>
    <div class="field half" style="left:619px;top:308px">Last Name</div>

    <div class="label" style="left:319px;top:350px">Phone<sup>*</sup></div>
    <div class="field wide" style="left:319px;top:368px"><span class="flag"></span><svg width="8" height="5" viewBox="0 0 8 5"><path d="M1 1l3 3 3-3" fill="none" stroke="#a8adb6"/></svg>&nbsp;&nbsp;Phone Number</div>
    <div class="label" style="left:619px;top:350px">DOB<sup>*</sup></div>
    <div class="field half" style="left:619px;top:368px">DD/MM/YYYY<svg class="chev" width="12" height="12" viewBox="0 0 12 12"><rect x="1" y="2" width="10" height="9" rx="1" fill="#1c2333"/><rect x="3" y="0" width="1.5" height="3" fill="#1c2333"/><rect x="7.5" y="0" width="1.5" height="3" fill="#1c2333"/><rect x="2" y="5" width="8" height="0.8" fill="#fff"/></svg></div>

    <div class="label" style="left:319px;top:410px">Email<sup>*</sup></div>
    <div class="field wide" style="left:319px;top:429px">Enter Email<svg class="chev" width="9" height="5" viewBox="0 0 9 5"><path d="M1 1l3.5 3 3.5-3" fill="none" stroke="#a8adb6"/></svg></div>
    <div class="label" style="left:619px;top:410px">Do You Have A Current Valid Driver’s Licence<sup>*</sup></div>
    <div class="field half" style="left:619px;top:429px">Yes / No<svg class="chev" width="9" height="5" viewBox="0 0 9 5"><path d="M1 1l3.5 3 3.5-3" fill="none" stroke="#a8adb6"/></svg></div>

    <div class="label" style="left:319px;top:471px">Do You Possess Your Own Smart Phone<sup>*</sup></div>
    <div class="field wide" style="left:319px;top:489px">Yes / No<svg class="chev" width="9" height="5" viewBox="0 0 9 5"><path d="M1 1l3.5 3 3.5-3" fill="none" stroke="#a8adb6"/></svg></div>
    <div class="label" style="left:619px;top:471px">An Is It: Plan/Prepaid ?</div>
    <div class="field half" style="left:619px;top:489px">Yes / No<svg class="chev" width="9" height="5" viewBox="0 0 9 5"><path d="M1 1l3.5 3 3.5-3" fill="none" stroke="#a8adb6"/></svg></div>

    <div class="label" style="left:319px;top:531px">Do You Have Your Own Reliable Transport<sup>*</sup></div>
    <div class="field wide" style="left:319px;top:550px">Yes / No<svg class="chev" width="9" height="5" viewBox="0 0 9 5"><path d="M1 1l3.5 3 3.5-3" fill="none" stroke="#a8adb6"/></svg></div>
    <div class="label" style="left:619px;top:531px">Do You Have A White Card<sup>*</sup></div>
    <div class="field half" style="left:619px;top:550px">Yes / No<svg class="chev" width="9" height="5" viewBox="0 0 9 5"><path d="M1 1l3.5 3 3.5-3" fill="none" stroke="#a8adb6"/></svg></div>

    <div class="label" style="left:319px;top:592px;width:250px">How Many Days A Week Would You Ideally Like To Work In This Cleaning Role? <span class="req">*</span></div>
    <div class="label" style="left:619px;top:592px;width:255px">Do You Have A Police Clearance Certificate Issued Within The Last 12 Months?<sup>*</sup></div>
    <div class="field half" style="left:619px;top:623px">Yes / No<svg class="chev" width="9" height="5" viewBox="0 0 9 5"><path d="M1 1l3.5 3 3.5-3" fill="none" stroke="#a8adb6"/></svg></div>

    <div class="check" style="left:319px;top:635px"><i></i>Monday</div>
    <div class="check" style="left:319px;top:655px"><i></i>Tuesday</div>
    <div class="check" style="left:319px;top:675px"><i></i>Wednesday</div>
    <div class="check" style="left:319px;top:695px"><i></i>Thursday</div>
    <div class="check" style="left:476px;top:635px"><i></i>Friday</div>
    <div class="check" style="left:476px;top:655px"><i></i>Saturday</div>
    <div class="check" style="left:476px;top:675px"><i></i>Sunday</div>

    <div class="label" style="left:319px;top:727px;width:250px">Do You Have Any Experience In Professional Cleaning? If Yes, Please State How Many Years. <span class="req">*</span></div>
    <div class="field wide" style="left:319px;top:759px">0 Years<svg class="chev" width="9" height="5" viewBox="0 0 9 5"><path d="M1 1l3.5 3 3.5-3" fill="none" stroke="#a8adb6"/></svg></div>
    <div class="label" style="left:631px;top:727px;width:250px">How Many Hours Per Week Would You Ideally Like To Work In This Cleaning Role?<sup>*</sup></div>
    <div class="field wide" style="left:631px;top:759px">Type Your Working Hours</div>

    <div class="label" style="left:319px;top:801px">Why Do You Want To Work For Plomver Services&nbsp; <span class="req">*</span></div>
    <div class="area" style="top:821px"></div>

    <div class="label" style="left:319px;top:914px">Do You Currently Have Any Other Commitments: Work, Study, Caring, Etc? <span class="req">*</span></div>
    <div class="area" style="top:934px"></div>

    <div class="label" style="left:319px;top:1027px;width:565px">Do You Have Any Pre-Exisiting Health Conditions Which May Impact You Ability To Do Physically Demanding Work? If So, Please State What They Are. <span class="req">*</span></div>
    <div class="area" style="top:1059px"></div>

    <div class="label" style="left:319px;top:1146px">Please Also Submit Your Resume With At Least 2 Referees From Prior Employment Or Work Experience.</div>
    <div class="note" style="top:1161px">We Do Not Accept Word Documents Resumes, Please Exports As Pdf In Orders To Upload.</div>
    <div class="drop"><span>Drop Files Here Or</span><b>SELECT FILES</b></div>
    <div class="note" style="top:1269px;font-size:6px;font-weight:600">Accepted File Types: Pdf, Jpg, Png, Max File Size: 10 MB.</div>

    <div class="small-caps">CAPTCHA</div>
    <div class="captcha"><i></i>I’m Not A Robot<span class="mark"></span></div>

    <div class="submit">SUBMIT</div>
  </section>

  <section class="cta" role="img" aria-label="Photo of a cleaner in an orange apron in a kitchen, teal to amber tint">
    <h2>Talk to our<br>experts today!</h2>
    <div class="btn teal">Book Online</div>
    <div class="btn orange">Contact Us For A Quote</div>
  </section>
</main>

<footer class="footer">
  <div class="brand"><span class="dot"></span>plomver services</div>
  <div class="contacts">
    <a><svg width="12" height="9" viewBox="0 0 12 9"><rect width="12" height="9" rx="1" fill="#2d9ad8"/><path d="M0.5 0.8L6 5l5.5-4.2" fill="none" stroke="#132240" stroke-width="1"/></svg><u>info@plomverservices.com.au</u></a>
    <a><svg width="8" height="12" viewBox="0 0 8 12"><rect x="0.7" y="0.7" width="6.6" height="10.6" rx="1.2" fill="none" stroke="#2d9ad8" stroke-width="1.3"/></svg><u>0400123987</u></a>
  </div>
  <div class="rule"></div>
  <div class="copy">© 2024 All Rights Reserved <b>By Plomver services</b></div>
  <nav class="links"><span>Home</span><span>About Us</span><span>Services</span><span>Terms &amp; Condition</span><span>Privacy Policy</span><span>Contact Us</span></nav>
</footer>
</body>
</html>
```